We are looking for a poster / flyer to advertise our Squash Tournament - the Wrenfold Club Sydney CBD Squash Open. I have provided the details and sponsor logos that need to appear on the poster in the attachments.
I am open to the poster including pictures of real life squash playing action shots or a complete graphic art design.

Target Market(s)

Squash Players and Sporty People who may be interested in trying Squash as a new Sport

Requirements
Must have
• 1. All logos attached in files (logos in the word doc and the Bramwick Logo)
2. Content that has been provided in the word doc
3. Printable on A3 paper
4. Title of the poster must be 2021 Wrenfold Club Sydney CBD Squash Open
Nice to have
• 1.Design must be related to the Sport of Squash (can either be a graphic Design that incorporates a real life squash pic rom the internet or 100% graphic)
2. Something incorporating both female and junior squash player participation.
3. Poster depicts action / athleticism.

```html
<!DOCTYPE html>
<html lang="en">
<head>
<meta charset="utf-8">
<title>2021 Wrenfold Club Sydney CBD Squash Open</title>
<link rel="stylesheet" href="https://fonts.googleapis.com/css2?family=Exo+2:wght@300;600;700;800&family=Open+Sans:wght@400;600&family=Archivo:wght@600&display=swap">
<style>
  :root{
    --stage:#5a5a5c;
    --navy:#1f2a6e;
    --navy-deep:#18215a;
    --yellow:#ffe800;
    --gold:#f6bd16;
    --heading-yellow:#f5e021;
    --tick:#5cb7ee;
    --white:#ffffff;
    --ink:#111111;
  }
  *{margin:0;padding:0;box-sizing:border-box}
  html,body{width:1200px;height:2864px;overflow:hidden;background:var(--stage)}
  .poster{position:absolute;left:0;top:582px;width:1200px;height:1700px;background:var(--navy);overflow:hidden;font-family:"Open Sans",sans-serif;color:var(--white)}
  .poster-shapes{position:absolute;inset:0;width:1200px;height:1700px}
  .t{position:absolute;line-height:1;white-space:nowrap}
  .year{left:78px;top:58px;font-family:"Exo 2",sans-serif;font-weight:800;font-size:200px;color:var(--gold);letter-spacing:-4px}
  .title{left:82px;top:258px;font-family:"Exo 2",sans-serif;font-weight:700;font-size:76px;line-height:84px}
  .sponsor-name{left:664px;top:100px;font-family:"Exo 2",sans-serif;font-weight:300;font-size:82px;color:var(--ink);letter-spacing:2px}
  .section-head{font-family:"Exo 2",sans-serif;font-weight:700;color:var(--heading-yellow)}
  .details-head{left:88px;top:568px;font-size:60px;line-height:64px}
  .ticks{position:absolute;left:86px;list-style:none;font-size:26px;line-height:35px}
  .ticks li{position:relative;padding-left:62px;margin-bottom:16px}
  .ticks svg{position:absolute;left:0;top:4px;width:28px;height:28px}
  .details-list{top:716px}
  .bar-note{left:84px;top:984px;font-family:"Archivo",sans-serif;font-weight:600;font-size:32px;line-height:36px;color:var(--navy-deep)}
  .grades-head{left:84px;top:1146px;font-size:37px}
  .grades-list{top:1200px}
  .grades-list li{margin-bottom:6px}
  .entry-fee{left:92px;top:1458px;font-size:38px}
  .entries{font-family:"Exo 2",sans-serif;font-weight:800;font-size:62px;color:var(--navy-deep);-webkit-text-stroke:2px var(--white);paint-order:stroke fill}
  .entries-close{left:716px;top:1294px}
  .entries-date{left:596px;top:1360px}
  .director-label{left:662px;top:1490px;font-family:"Exo 2",sans-serif;font-weight:600;font-size:36px}
  .contact{color:var(--navy-deep)}
  .contact-name{left:806px;top:1548px;font-family:"Exo 2",sans-serif;font-weight:700;font-size:34px}
  .contact-phone{left:840px;top:1590px;font-family:"Exo 2",sans-serif;font-weight:700;font-size:48px}
  .contact-phone svg{position:absolute;left:-34px;top:14px;width:26px;height:26px}
  .contact-email{left:850px;top:1648px;font-family:"Open Sans",sans-serif;font-weight:600;font-size:20px}
  .contact-email svg{position:absolute;left:-34px;top:2px;width:24px;height:18px}
  .partner{position:absolute;font-family:"Exo 2",sans-serif;font-weight:700;font-size:24px;color:var(--navy);display:flex;align-items:center;gap:8px;line-height:1}
  .partner .mark{width:18px;height:18px;border-radius:50%;background:var(--gold)}
  .partner-uni{left:96px;top:1588px}
  .partner-metro{left:268px;top:1588px}
  .partner-club{left:466px;top:1570px}
  .partner-halloway{left:466px;top:1616px}
</style>
</head>
<body>
<main class="poster">
  <svg class="poster-shapes" viewBox="0 0 1200 1700">
    <defs>
      <linearGradient id="bandGrad" x1="0" y1="0" x2="1" y2="1">
        <stop offset="0" stop-color="#3e468f"/>
        <stop offset="0.6" stop-color="#8f91cc"/>
        <stop offset="1" stop-color="#d9daf0"/>
      </linearGradient>
      <linearGradient id="courtGrad" x1="0" y1="0" x2="0" y2="1">
        <stop offset="0" stop-color="#f6f3f1"/>
        <stop offset="1" stop-color="#e9dfd6"/>
      </linearGradient>
    </defs>
    <polygon points="531,0 1200,0 1200,700 1110,800" fill="var(--white)"/>
    <polygon role="img" aria-label="Photo of a squash player in a pink top waiting for a shot on court" points="1000,0 1200,0 1200,700 1110,800 1000,600" fill="url(#courtGrad)"/>
    <polygon role="img" aria-label="Action photo of a female squash player in an orange shirt lunging to play a shot" points="531,0 1110,800 1200,700 1200,1250 1020,1460 620,880 560,560 860,560" fill="url(#bandGrad)" opacity="0.95"/>
    <polygon points="720,952 484,1277 600,1445 1050,1445 1200,1290 1200,1560 980,1560 1000,1445" fill="var(--yellow)"/>
    <!-- yellow contact corner -->
    <polygon points="700,1700 790,1532 1090,1532 1200,1380 1200,1700" fill="var(--yellow)"/>
    <polygon points="597,1474 1131,1474 1090,1532 560,1532" fill="var(--navy-deep)"/>
    <polygon points="0,964 659,964 600,1115 0,1115" fill="var(--yellow)"/>
    <polygon points="21,1535 780,1535 740,1666 21,1666" fill="var(--white)"/>
    <line x1="26" y1="1545" x2="74" y2="1660" stroke="var(--navy)" stroke-width="3"/>
    <line x1="46" y1="1545" x2="94" y2="1660" stroke="var(--navy)" stroke-width="3"/>
  </svg>

  <div class="t year">2021</div>
  <h1 class="t title">Wrenfold Club<br>Sydney CBD<br>Squash Open</h1>
  <div class="t sponsor-name">BRAMWICK</div>

  <h2 class="t section-head details-head">Tournament<br>Details</h2>
  <ul class="ticks details-list">
    <li><svg viewBox="0 0 28 28"><circle cx="14" cy="14" r="11" fill="none" stroke="var(--tick)" stroke-width="2.5"/><path d="M8 14l5 5 10-12" fill="none" stroke="var(--tick)" stroke-width="2.5"/></svg>13 th – 15th August 2021</li>
    <li><svg viewBox="0 0 28 28"><circle cx="14" cy="14" r="11" fill="none" stroke="var(--tick)" stroke-width="2.5"/><path d="M8 14l5 5 10-12" fill="none" stroke="var(--tick)" stroke-width="2.5"/></svg>Held at CBD Courts (Wrenfold<br>&amp; Halloway Clubs) and<br>Harbour Uni. Sport &amp; Fitness</li>
    <li><svg viewBox="0 0 28 28"><circle cx="14" cy="14" r="11" fill="none" stroke="var(--tick)" stroke-width="2.5"/><path d="M8 14l5 5 10-12" fill="none" stroke="var(--tick)" stroke-width="2.5"/></svg>All finals will be at the Wrenfold Club</li>
  </ul>

  <p class="t bar-note">SATURDAY NIGHT OPEN BAR<br>IN CBD PROVIDED BY<br>SPONSOR ($3K BAR TAB)</p>

  <h2 class="t section-head grades-head">Grades Available:-</h2>
  <ul class="ticks grades-list">
    <li><svg viewBox="0 0 28 28"><circle cx="14" cy="14" r="11" fill="none" stroke="var(--tick)" stroke-width="2.5"/><path d="M8 14l5 5 10-12" fill="none" stroke="var(--tick)" stroke-width="2.5"/></svg>Mens and Ladies Squash<br>Open, $14k in prizemoney</li>
    <li><svg viewBox="0 0 28 28"><circle cx="14" cy="14" r="11" fill="none" stroke="var(--tick)" stroke-width="2.5"/><path d="M8 14l5 5 10-12" fill="none" stroke="var(--tick)" stroke-width="2.5"/></svg>Junior events</li>
    <li><svg viewBox="0 0 28 28"><circle cx="14" cy="14" r="11" fill="none" stroke="var(--tick)" stroke-width="2.5"/><path d="M8 14l5 5 10-12" fill="none" stroke="var(--tick)" stroke-width="2.5"/></svg>Racquetball Open</li>
    <li><svg viewBox="0 0 28 28"><circle cx="14" cy="14" r="11" fill="none" stroke="var(--tick)" stroke-width="2.5"/><path d="M8 14l5 5 10-12" fill="none" stroke="var(--tick)" stroke-width="2.5"/></svg>All grades / abilities catered for<br>Players guaranteed</li>
  </ul>
  <div class="t section-head entry-fee">3 matches $60 entry fee</div>

  <div class="t entries entries-close">Entries close</div>
  <div class="t entries entries-date">7th August 2021</div>

  <div class="t director-label">Tournament Director</div>
  <div class="t contact contact-name">Daniel Ashcombe</div>
  <div class="t contact contact-phone"><svg viewBox="0 0 24 24"><path d="M6 2l4 4-2 3c1 3 4 6 7 7l3-2 4 4-3 4C10 22 2 14 2 5z" fill="var(--navy-deep)"/></svg>0412555908</div>
  <div class="t contact contact-email"><svg viewBox="0 0 24 18"><rect x="1" y="1" width="22" height="16" fill="var(--navy-deep)"/><path d="M1 1l11 9 11-9" fill="none" stroke="var(--yellow)" stroke-width="2"/></svg>daniel.ashcombe@mailbox.test</div>

  <div class="partner partner-uni"><span class="mark"></span>Harbour Uni</div>
  <div class="partner partner-metro"><span class="mark"></span>Metro Squash</div>
  <div class="partner partner-club">Wrenfold Club</div>
  <div class="partner partner-halloway">Halloway</div>
</main>
</body>
</html>
```